Burlgrain Joinery eye catching business card

I need an eye catching business card that reflects my traditional, fun, handmade woodcraft shop. I make high end custom furniture and fine woodworking products, a lot of which are rustic, natural looking. We are a small shop but we produce awesome, one of a kind wood products, and our business card should reflect that. Our target audience is young professionals to retired folks who want a quality, local, handmade product. I'd like the Shop Nearby logo somewhere on the card, BUT not overwhelming, the main focus is my Logo, no preference on color whichever looks the best. Visit my website to get a feel for my company. Burlgrainjoinery.com
Target Market(s)
young professionals to retired folks. Any one who wants to furnish their home with quality handcrafted products.
Industry/Entity Type
Business
Contact Information for Business Card
Dale Merriwick (555)417-6293
dale@burlgrainjoinery.com
www.burlgrainjoinery.com

```html
<!DOCTYPE html>
<html lang="en">
<head>
<meta charset="utf-8">
<title>Burlgrain Joinery – Business Card</title>
<link href="https://fonts.googleapis.com/css2?family=Cinzel:wght@400;600&family=Montserrat:wght@300;400&display=swap" rel="stylesheet">
<style>
  :root {
    --page-bg: #efece6;
    --card-white: #ffffff;
    --wood-light: #9a9180;
    --wood-mid: #7b7262;
    --wood-dark: #5b5346;
    --logo-cream: #f4f1ea;
    --brand-olive: #8f8459;
    --text-olive: #a59a70;
    --card-shadow: rgba(40, 30, 20, 0.18);
  }
  * { margin: 0; padding: 0; box-sizing: border-box; }
  html, body {
    width: 1200px;
    height: 1000px;
    overflow: hidden;
    background: var(--page-bg);
  }
  .sheet {
    width: 1200px;
    height: 1000px;
    display: flex;
    flex-direction: column;
    align-items: center;
    justify-content: center;
    gap: 60px;
  }
  .card {
    width: 700px;
    height: 400px;
    box-shadow: 0 10px 30px var(--card-shadow);
    position: relative;
    overflow: hidden;
  }
  .card-front {
    display: flex;
    align-items: center;
    justify-content: center;
  }
  .wood-texture {
    position: absolute;
    inset: 0;
    background: linear-gradient(100deg, var(--wood-light) 0%, var(--wood-mid) 45%, var(--wood-light) 70%, var(--wood-dark) 100%);
  }
  .front-logo {
    position: relative;
    font-family: "Cinzel", serif;
    font-weight: 600;
    font-size: 54px;
    letter-spacing: 4px;
    color: var(--logo-cream);
    text-transform: uppercase;
    text-align: center;
    line-height: 1.1;
  }
  .card-back {
    background: var(--card-white);
    display: flex;
    flex-direction: column;
    align-items: center;
    justify-content: center;
    gap: 22px;
  }
  .back-name {
    font-family: "Cinzel", serif;
    font-weight: 400;
    font-size: 38px;
    letter-spacing: 3px;
    color: var(--brand-olive);
    text-transform: uppercase;
  }
  .back-web,
  .back-contact {
    font-family: "Montserrat", sans-serif;
    font-weight: 300;
    font-size: 14px;
    letter-spacing: 1.5px;
    color: var(--text-olive);
    text-transform: uppercase;
  }
  .back-contact { margin-top: 14px; }
</style>
</head>
<body>
  <main class="sheet">
    <section class="card card-front">
      <div class="wood-texture" role="img" aria-label="Weathered grey oak plank texture with knots"></div>
      <h1 class="front-logo">Burlgrain<br>Joinery</h1>
    </section>
    <section class="card card-back">
      <h2 class="back-name">Burlgrain Joinery</h2>
      <p class="back-web">www.burlgrainjoinery.com</p>
      <p class="back-contact">Dale Merriwick | dale@burlgrainjoinery.com | (555)417-6293</p>
    </section>
  </main>
</body>
</html>
```